Larkmont Business Card Design Project

Double side card , just the logo on oxford white background on one side , and the rest of the information on the other side..
the company name is : Larkmont International General Trading LLC.
logo is already attached
the card to show in the info side: company name, employee name and position (job title) phone number, fax number, email address, P.O. box, Location (city and country)
deadline is already extended 4 all to have more time... thanks

```html
<!DOCTYPE html>
<html lang="en">
<head>
<meta charset="utf-8">
<title>Larkmont International General Trading LLC. – Business Card</title>
<link rel="stylesheet" href="https://fonts.googleapis.com/css2?family=Montserrat:wght@800&family=Noto+Sans:wght@300&display=swap">
<style>
  :root {
    --card-turquoise: #54ffe1;
    --card-white: #ffffff;
  }
  html, body {
    margin: 0;
    padding: 0;
    overflow: hidden;
    background: var(--card-turquoise);
  }
  .card {
    position: relative;
    width: 1200px;
    height: 702px;
    background: var(--card-turquoise);
    color: var(--card-white);
    overflow: hidden;
  }
  .company-name {
    position: absolute;
    left: 60px;
    top: 103px;
    margin: 0;
    font-family: "Montserrat", sans-serif;
    font-weight: 800;
    font-size: 63px;
    line-height: 53px;
    text-transform: uppercase;
    letter-spacing: -0.3px;
  }
  .company-name span { display: block; }
  .divider {
    position: absolute;
    left: 59px;
    top: 317px;
    width: 760px;
    height: 7px;
    background: var(--card-white);
  }
  .logo-badge {
    position: absolute;
    left: 789px;
    top: 51px;
    width: 356px;
    height: 356px;
    border-radius: 50%;
    background: var(--card-white);
    display: flex;
    align-items: center;
    justify-content: center;
    text-align: center;
    font-family: "Montserrat", sans-serif;
    font-weight: 800;
    font-size: 51px;
    line-height: 44px;
    color: var(--card-turquoise);
    text-transform: uppercase;
  }
  .person-name {
    position: absolute;
    left: 77px;
    top: 347px;
    margin: 0;
    font-family: "Montserrat", sans-serif;
    font-weight: 800;
    font-size: 34px;
    line-height: 34px;
    text-transform: uppercase;
  }
  .job-title {
    position: absolute;
    left: 77px;
    top: 379px;
    margin: 0;
    font-family: "Noto Sans", sans-serif;
    font-weight: 300;
    font-size: 24px;
    line-height: 24px;
  }
  .contact-list,
  .address {
    position: absolute;
    margin: 0;
    font-family: "Noto Sans", sans-serif;
    font-weight: 300;
    font-size: 27px;
    line-height: 33.5px;
    font-style: normal;
  }
  .contact-list {
    left: 64px;
    top: 519px;
    padding: 0;
    list-style: none;
  }
  .address {
    right: 63px;
    top: 554px;
    text-align: right;
  }
</style>
</head>
<body>
  <main class="card">
    <h1 class="company-name">
      <span>Larkmont</span>
      <span>International</span>
      <span>General</span>
      <span>Trading LLC</span>
    </h1>
    <div class="divider"></div>
    <div class="logo-badge">Logo<br>Here</div>

    <p class="person-name">John Doe Smith</p>
    <p class="job-title">Job Title Senior Editor</p>

    <ul class="contact-list">
      <li>Sample phone number</li>
      <li>Sample Fax Number</li>
      <li>sample.email@larkmail.com</li>
    </ul>

    <address class="address">
      Sample P.O. box,<br>
      Location (city and country)
    </address>
  </main>
</body>
</html>
```